Brisbane IT support business needs our first business card

Hello we are a Brisbane based Information Technology company providing support and services to small and medium sized businesses. We provide a range of services and solutions.

The business name is Wattleridge Computer Services Group, or WCSG for short.

I am looking for a business card that looks professional (don't we all want that), but most importantly, it most utilize the colours in the logo attached.

Other business owners seeking our IT services, and also home users.

Business

• Please only use the blue/orange colours in logo attached

```html
<!DOCTYPE html>
<html lang="en">
<head>
<meta charset="utf-8">
<title>WCSG Business Card</title>
<link rel="stylesheet" href="https://fonts.googleapis.com/css2?family=Lato:wght@400;700;900&display=swap">
<style>
  :root {
    --navy: #0b4a63;
    --orange: #ef7d22;
    --white: #ffffff;
    --ink: #173c52;
    --backdrop: #e9ecef;
  }
  * { margin: 0; padding: 0; box-sizing: border-box; }
  html, body { width: 1200px; height: 900px; overflow: hidden; }
  body {
    background: var(--backdrop);
    font-family: "Lato", Arial, sans-serif;
    position: relative;
  }
  .card {
    position: absolute;
    left: 260px;
    width: 680px;
    height: 390px;
    border-radius: 16px;
    overflow: hidden;
    box-shadow: 0 6px 18px rgba(0,0,0,0.18);
  }
  /* Back side */
  .card-back { top: 40px; background: var(--navy); }
  .back-disc {
    position: absolute;
    left: -130px; top: 130px;
    width: 400px; height: 400px;
    border-radius: 50%;
    background: var(--white);
  }
  .back-brand { position: absolute; left: 330px; top: 70px; }
  .back-brand .brand-mark {
    font-weight: 900; font-size: 112px; line-height: 1;
    color: var(--orange); letter-spacing: 2px;
  }
  .back-brand .brand-full {
    margin-top: 6px; width: 300px;
    font-weight: 700; font-size: 19px; line-height: 1.15;
    color: var(--white); text-transform: uppercase; letter-spacing: 0.5px;
  }
  /* Front side */
  .card-front { top: 470px; background: var(--white); }
  .front-brand { position: absolute; left: 42px; top: 34px; display: flex; align-items: center; gap: 16px; }
  .brand-dot { width: 62px; height: 62px; border-radius: 50%; background: var(--navy); }
  .front-brand .brand-mark {
    font-weight: 900; font-size: 42px; line-height: 1; color: var(--orange); letter-spacing: 1px;
  }
  .front-brand .brand-full {
    margin-top: 3px; font-weight: 700; font-size: 10.5px; line-height: 1.15;
    color: var(--ink); text-transform: uppercase; width: 200px;
  }
  .holder { position: absolute; left: 56px; top: 130px; }
  .holder-name { font-size: 27px; font-weight: 400; color: var(--orange); }
  .holder-role { font-size: 16px; color: var(--ink); margin-top: 2px; }
  .contacts { position: absolute; left: 56px; top: 205px; list-style: none; }
  .contacts li {
    display: flex; align-items: center; gap: 12px;
    font-size: 17px; color: var(--ink); height: 24px;
  }
  .contacts svg { width: 18px; height: 18px; fill: var(--orange); flex: none; }
  .address {
    position: absolute; left: 56px; top: 316px;
    font-size: 17px; line-height: 1.3; color: var(--ink);
  }
  .front-disc {
    position: absolute;
    left: 500px; top: 70px;
    width: 300px; height: 300px;
    border-radius: 50%;
    background: var(--navy);
  }
</style>
</head>
<body>
  <section class="card card-back" aria-label="Card back">
    <div class="back-disc" role="img" aria-label="City skyline silhouette"></div>
    <div class="back-brand">
      <div class="brand-mark">WCSG</div>
      <div class="brand-full">Wattleridge Computer Services Group</div>
    </div>
  </section>

  <section class="card card-front" aria-label="Card front">
    <div class="front-brand">
      <div class="brand-dot"></div>
      <div>
        <div class="brand-mark">WCSG</div>
        <div class="brand-full">Wattleridge Computer Services Group</div>
      </div>
    </div>

    <div class="holder">
      <div class="holder-name">Harlan Pemberton</div>
      <div class="holder-role">Director</div>
    </div>

    <ul class="contacts">
      <li>
        <svg viewBox="0 0 24 24" aria-hidden="true"><path d="M6.6 10.8a15.1 15.1 0 0 0 6.6 6.6l2.2-2.2c.3-.3.7-.4 1-.2 1.1.4 2.3.6 3.6.6.6 0 1 .4 1 1V20c0 .6-.4 1-1 1A17 17 0 0 1 3 4c0-.6.4-1 1-1h3.5c.6 0 1 .4 1 1 0 1.3.2 2.5.6 3.6.1.3 0 .7-.2 1z"/></svg>
        123 456 7890
      </li>
      <li>
        <svg viewBox="0 0 24 24" aria-hidden="true"><path d="M8 1h8a2 2 0 0 1 2 2v18a2 2 0 0 1-2 2H8a2 2 0 0 1-2-2V3a2 2 0 0 1 2-2zm0 3v14h8V4zm4 15.5a1 1 0 1 0 0 2 1 1 0 0 0 0-2z"/></svg>
        123 456 7890
      </li>
      <li>
        <svg viewBox="0 0 24 24" aria-hidden="true"><path d="M2 5h20v14H2zm2 2v.5l8 5 8-5V7zm0 2.8V17h16V9.8l-8 5z"/></svg>
        yourname@wcsg.com.au
      </li>
      <li>
        <svg viewBox="0 0 24 24" aria-hidden="true"><path d="M12 2a10 10 0 1 0 0 20 10 10 0 0 0 0-20zm6.9 6h-3a15 15 0 0 0-1.3-3.9A8 8 0 0 1 18.9 8zM12 4c.8 1.2 1.5 2.5 1.9 4h-3.8c.4-1.5 1.1-2.8 1.9-4zM4.3 14a8 8 0 0 1 0-4h3.4a16 16 0 0 0 0 4zm.8 2h3a15 15 0 0 0 1.3 3.9A8 8 0 0 1 5.1 16zm3-8h-3a8 8 0 0 1 4.3-3.9A15 15 0 0 0 8.1 8zM12 20c-.8-1.2-1.5-2.5-1.9-4h3.8c-.4 1.5-1.1 2.8-1.9 4zm2.3-6H9.7a14 14 0 0 1 0-4h4.6a14 14 0 0 1 0 4zm.3 5.9a15 15 0 0 0 1.3-3.9h3a8 8 0 0 1-4.3 3.9zM16.3 14a16 16 0 0 0 0-4h3.4a8 8 0 0 1 0 4z"/></svg>
        www.wcsg.com.au
      </li>
    </ul>

    <address class="address" style="font-style: normal;">
      12-13 Suite, Kelvin Road, Brisbane<br>QLD 4000
    </address>

    <div class="front-disc" role="img" aria-label="City skyline silhouette"></div>
  </section>
</body>
</html>
```